Postcard Design

Income tax servicesOver 20 years experienceBusiness and Personal Tax ReturnsAll State ReturnsFree Electronic FilingI would like a simple map showing how to get to my house.reasons to use a tax preparerYou don’t have to keep up with the many tax law changes or understand complicated tax law.Your time is worth money – add up the hours you would spend doing it yourself and calculate what that’s worth.A tax program in a box cannot represent you in an audit.A tax professional can answer your questions to help you make smarter tax-saving decisions.It gives you peace of mind knowing that a professional is taking care of it.It can save you money – if your tax preparer finds even one significant deduction or tax credit you may have missed, it can easily cover the cost to have them prepared.Going to be targeting the area within 2 square miles of my home office so would like to promote proximity to the possible clients
Electronic

```html
<!DOCTYPE html>
<html lang="en">
<head>
<meta charset="utf-8">
<title>Income Tax Services Postcard</title>
<link href="https://fonts.googleapis.com/css2?family=Fjalla+One&family=Ubuntu:wght@400;500;700&display=swap" rel="stylesheet">
<style>
  :root{
    --blue:#1b63b0;
    --blue-dark:#0f4a8e;
    --blue-light:#2a86cf;
    --orange:#f7941d;
    --orange-deep:#ee5a24;
    --yellow:#ffc20e;
    --ink:#3a3a3a;
    --white:#ffffff;
    --stage:#d9d6d2;
    --photo-dark:#1b1b1b;
    --photo-mid:#5b5550;
  }
  *{box-sizing:border-box;margin:0;padding:0}
  html,body{width:874px;height:1200px;overflow:hidden}
  body{background:var(--stage);position:relative;font-family:'Ubuntu',sans-serif}
  .card{position:absolute;left:73px;width:725px;height:517px;overflow:hidden;box-shadow:0 4px 14px rgba(0,0,0,.35)}
  .card--front{top:66px;background:var(--photo-dark)}
  .card--back{top:625px;background:var(--white)}
  .layer{position:absolute;left:0;top:0}
  .headline{font-family:'Fjalla One',sans-serif;color:var(--white);position:absolute}
  .front__title{left:29px;top:18px;font-size:46px;line-height:1}
  .front__subtitle{left:29px;top:78px;font-size:24px;line-height:1}
  .photo-area{position:absolute;left:0;top:140px;width:725px;height:340px;
    background:linear-gradient(115deg,var(--photo-mid) 0%,#2a2624 40%,var(--photo-dark) 60%,#3a3836 100%)}
  .photo-area--paper{position:absolute;right:0;bottom:0;width:520px;height:110px;
    background:linear-gradient(170deg,rgba(255,255,255,0) 0%,rgba(230,230,232,.85) 40%,#f2f2f4 100%)}
  .feature-list{position:absolute;right:39px;top:196px;list-style:none;text-align:right}
  .feature-list li{font-family:'Fjalla One',sans-serif;color:var(--yellow);font-size:35px;line-height:48px;display:flex;align-items:center;justify-content:flex-end;gap:12px}
  .feature-list svg{width:34px;height:34px}
  .badge{position:absolute;left:526px;top:22px;width:128px;height:128px}
  .brand-box{position:absolute;left:23px;top:432px;width:209px;height:72px;background:var(--white);display:flex;flex-direction:column;align-items:center;justify-content:center;gap:6px}
  .brand-name{display:flex;align-items:center;gap:7px;font-family:'Ubuntu',sans-serif;font-weight:700;color:var(--ink);font-size:22px;line-height:1}
  .brand-name i{display:block;width:14px;height:14px;border-radius:50%;background:var(--ink)}
  .brand-tagline{font-size:9.5px;color:var(--ink)}
  .contact-bar{position:absolute;left:0;top:477px;width:725px;height:40px;background:var(--blue);display:flex;align-items:center}
  .contact-bar__web{position:absolute;left:258px;color:var(--white);font-weight:700;font-size:19px}
  .contact-bar__sep{position:absolute;left:563px;top:8px;width:1px;height:24px;background:rgba(255,255,255,.7)}
  .contact-bar__phone{position:absolute;left:580px;color:var(--white);font-weight:700;font-size:19px}

  .back__heading{position:absolute;left:23px;top:24px;font-family:'Ubuntu',sans-serif;font-weight:500;font-size:27px;color:var(--blue)}
  .reasons{position:absolute;left:23px;top:74px;width:361px;list-style:none}
  .reasons li{position:relative;padding-left:21px;font-size:13px;line-height:17.5px;color:var(--ink);margin-bottom:9px;text-align:justify}
  .reasons svg{position:absolute;left:0;top:2px;width:13px;height:13px}
  .divider{position:absolute;left:406px;top:55px;width:1px;height:323px;background:var(--orange)}
  .back-brand{position:absolute;left:460px;top:24px;width:212px;display:flex;flex-direction:column;align-items:center;gap:8px}
  .back__title{position:absolute;left:420px;top:80px;width:290px;text-align:center;font-family:'Fjalla One',sans-serif;color:var(--orange);font-size:46px;line-height:48px}
  .illustration{position:absolute;left:418px;top:185px;width:290px;height:225px;border-radius:40% 30% 0 0;
    background:radial-gradient(circle at 35% 45%,#f4f4f4 0%,#e9e9e9 45%,rgba(233,233,233,0) 46%),linear-gradient(160deg,#ffffff 40%,#8fd3e0 75%,#2bb3c9 100%)}
  .back__footer{position:absolute;left:0;top:0}
  .call-now{position:absolute;left:29px;top:472px;color:var(--white);font-weight:700;font-size:17px}
  .call-now strong{font-family:'Fjalla One',sans-serif;font-weight:400;font-size:24px;letter-spacing:.5px}
  .preparer{position:absolute;right:39px;top:432px;font-family:'Fjalla One',sans-serif;color:var(--white);font-size:29px;line-height:36px;text-align:right}
  .preparer-email{position:absolute;right:39px;top:474px;color:var(--white);font-weight:700;font-size:16.5px;text-align:right}
</style>
</head>
<body>

<section class="card card--front">
  <div class="photo-area" role="img" aria-label="Photo of a hand signing a tax document with a fountain pen">
    <div class="photo-area--paper"></div>
  </div>

  <svg class="layer" width="725" height="517" viewBox="0 0 725 517" aria-hidden="true">
    <path d="M0 110C80 160 160 185 260 160 380 130 520 100 725 140V158C560 128 430 140 330 160 210 186 110 196 0 150Z" fill="var(--orange)"/>
    <path d="M0 0H725V125C560 110 420 115 320 130 210 150 110 150 0 110Z" fill="var(--blue)"/>
    <path d="M0 0H725V70C500 40 250 40 0 80Z" fill="var(--blue-dark)" opacity=".35"/>
  </svg>

  <h1 class="headline front__title">Income Tax Services</h1>
  <p class="headline front__subtitle">Business and Personal Tax Returns</p>

  <svg class="badge" viewBox="0 0 128 128" aria-label="20 years experience">
    <defs>
      <path id="arc-top" d="M22 64A42 42 0 0 1 106 64"/>
      <path id="arc-bottom" d="M18 64A46 46 0 0 0 110 64"/>
      <radialGradient id="badge-core" cx="50%" cy="40%" r="60%">
        <stop offset="0" stop-color="#ffd25a"/><stop offset="1" stop-color="#f7941d"/>
      </radialGradient>
    </defs>
    <circle cx="64" cy="64" r="63" fill="#e8e8e8"/>
    <circle cx="64" cy="64" r="60" fill="#ffffff"/>
    <circle cx="64" cy="64" r="37" fill="url(#badge-core)" stroke="#555" stroke-width="2"/>
    <text font-family="Fjalla One, sans-serif" font-size="15" fill="#333" letter-spacing="2"><textPath href="#arc-top" startOffset="50%" text-anchor="middle">EXPERIENCE</textPath></text>
    <text font-family="Fjalla One, sans-serif" font-size="15" fill="#333" letter-spacing="2"><textPath href="#arc-bottom" startOffset="50%" text-anchor="middle">EXPERIENCE</textPath></text>
    <text x="64" y="72" text-anchor="middle" font-family="Fjalla One, sans-serif" font-size="42" fill="#1a1a1a">20</text>
    <text x="64" y="90" text-anchor="middle" font-family="Fjalla One, sans-serif" font-size="15" fill="#1a1a1a">years</text>
  </svg>

  <ul class="feature-list">
    <li>All State Returns <svg viewBox="0 0 24 24"><path d="M3 13l6 6L21 4" fill="none" stroke="#fff" stroke-width="3.2" stroke-linecap="round" stroke-linejoin="round"/></svg></li>
    <li>Free Electronic Filing <svg viewBox="0 0 24 24"><path d="M3 13l6 6L21 4" fill="none" stroke="#fff" stroke-width="3.2" stroke-linecap="round" stroke-linejoin="round"/></svg></li>
  </ul>

  <div class="contact-bar">
    <span class="contact-bar__web">www.cedarrowtax.com</span>
    <span class="contact-bar__sep"></span>
    <span class="contact-bar__phone">555-014-2637</span>
  </div>

  <div class="brand-box">
    <span class="brand-name"><i></i>Cedar Row Tax</span>
    <span class="brand-tagline">Your neighborhood tax office</span>
  </div>
</section>

<section class="card card--back">
  <h2 class="back__heading">Reasons to use a tax preparer</h2>
  <ul class="reasons">
    <li><svg viewBox="0 0 14 14"><circle cx="7" cy="7" r="6" fill="#1b63b0"/><path d="M4 7l2 2 4-5" fill="none" stroke="#fff" stroke-width="1.6"/></svg>You don’t have to keep up with the many tax law changes or understand complicated tax law.</li>
    <li><svg viewBox="0 0 14 14"><circle cx="7" cy="7" r="6" fill="#1b63b0"/><path d="M4 7l2 2 4-5" fill="none" stroke="#fff" stroke-width="1.6"/></svg>Your time is worth money – add up the hours you would spend doing it yourself and calculate what that’s worth.</li>
    <li><svg viewBox="0 0 14 14"><circle cx="7" cy="7" r="6" fill="#1b63b0"/><path d="M4 7l2 2 4-5" fill="none" stroke="#fff" stroke-width="1.6"/></svg>A tax program in a box cannot represent you in an audit.</li>
    <li><svg viewBox="0 0 14 14"><circle cx="7" cy="7" r="6" fill="#1b63b0"/><path d="M4 7l2 2 4-5" fill="none" stroke="#fff" stroke-width="1.6"/></svg>A tax professional can answer your questions to help you make smarter tax-saving decisions.</li>
    <li><svg viewBox="0 0 14 14"><circle cx="7" cy="7" r="6" fill="#1b63b0"/><path d="M4 7l2 2 4-5" fill="none" stroke="#fff" stroke-width="1.6"/></svg>It gives you peace of mind knowing that a professional is taking care of it.</li>
    <li><svg viewBox="0 0 14 14"><circle cx="7" cy="7" r="6" fill="#1b63b0"/><path d="M4 7l2 2 4-5" fill="none" stroke="#fff" stroke-width="1.6"/></svg>It can save you money – if your tax preparer finds even one significant deduction or tax credit you may have missed, it can easily cover the cost to have them prepared.</li>
    <li><svg viewBox="0 0 14 14"><circle cx="7" cy="7" r="6" fill="#1b63b0"/><path d="M4 7l2 2 4-5" fill="none" stroke="#fff" stroke-width="1.6"/></svg>Going to be targeting the area within 2 square miles of my home office so would like to promote proximity to the possible clients</li>
  </ul>

  <div class="divider"></div>

  <div class="back-brand">
    <span class="brand-name"><i></i>Cedar Row Tax</span>
    <span class="brand-tagline">Your neighborhood tax office</span>
  </div>
  <h2 class="back__title">Income Tax<br>Services</h2>

  <div class="illustration" role="img" aria-label="Illustration of a woman drawing a clock labelled time for taxes"></div>

  <svg class="back__footer" width="725" height="517" viewBox="0 0 725 517" aria-hidden="true">
    <path d="M0 420C60 440 120 458 200 455 300 451 400 424 500 408 580 396 660 402 725 426V517H0Z" fill="#ee5a24"/>
    <path d="M0 426C60 446 120 462 200 460 300 456 400 428 500 412 580 400 660 406 725 432V517H0Z" fill="#f7941d"/>
    <path d="M0 440C60 458 130 476 210 474 320 468 420 440 520 420 600 406 670 414 725 442V517H0Z" fill="#1b63b0"/>
    <path d="M0 480C200 505 500 450 725 485V517H0Z" fill="#2a86cf" opacity=".35"/>
  </svg>

  <p class="call-now">Call Now Today : <strong>555-014-2637</strong></p>
  <p class="preparer">Martin Hale, CPA</p>
  <p class="preparer-email">email: office@cedarrowtax.com</p>
</section>

</body>
</html>
```